ALL TEXT GRAPHICS TM May 2025 for Instagram

We are looking for a series of social media graphics for Instagram (new size: 4:5 (1080 x 1350 pixels) ratio that are ALL TEXT. We want the following quotes below on each graphic; one quote per graphic. AND, In very small letters at the bottom of each graphic, add @TovaMarshOnline
The look and feel of these graphics should be complimentary to the color palette attached below; but keep them simple. But the design is up to you; at the end of this document, I provided various samples of all text graphics that I like as examples.
Target Market(s)
women looking to lose weight
Look and feel

```html
<!DOCTYPE html>
<html lang="en">
<head>
<meta charset="utf-8">
<title>TM All-Text Instagram Graphics</title>
<link rel="stylesheet" href="https://fonts.googleapis.com/css2?family=Bebas+Neue&family=Quicksand:wght@400&display=swap">
<style>
  :root {
    --canvas: #ffffff;
    --ink-dark: #231f20;
    --magenta: #f0086f;
    --hot-pink: #ff0599;
    --soft-pink: #fe8fc8;
    --blush: #fdd0e6;
    --bubblegum: #ff8cc8;
    --accent: #e0005f;
    --text-light: #efe9ea;
    --text-pale: #fbc9e3;
    --text-deep: #e2005f;
  }
  * { margin: 0; padding: 0; box-sizing: border-box; }
  html, body {
    width: 1200px; height: 811px; overflow: hidden;
    background: var(--canvas);
  }
  .series { position: relative; width: 1200px; height: 811px; }
  .post {
    position: absolute; top: 198px;
    width: 344px; height: 430px;
    overflow: hidden;
  }
  .post--dark {
    left: 47px;
    background: radial-gradient(ellipse 62% 58% at 50% 44%, var(--magenta) 0%, #b30c55 45%, var(--ink-dark) 100%);
  }
  .post--hot {
    left: 418px;
    background: radial-gradient(ellipse 60% 55% at 50% 50%, var(--soft-pink) 0%, #ff5ab2 50%, var(--hot-pink) 100%);
  }
  .post--soft {
    left: 787px;
    background: radial-gradient(ellipse 60% 55% at 50% 50%, var(--blush) 0%, #fdb3d9 50%, var(--bubblegum) 100%);
  }
  .corner { position: absolute; right: 0; bottom: 0; width: 96px; height: 97px; }
  .corner polygon { fill: var(--accent); }
  .quote {
    position: absolute;
    font-family: "Bebas Neue", "Oswald", sans-serif;
    white-space: nowrap;
  }
  .quote span { display: block; }
  .post--dark .quote {
    left: 49px; top: 160px;
    font-size: 30px; line-height: 27.5px;
    color: var(--text-light);
  }
  .post--hot .quote {
    left: 59px; top: 62px;
    font-size: 38px; line-height: 41.5px;
    color: var(--text-pale);
  }
  .post--hot .quote .indent { padding-left: 7px; }
  .post--soft .quote {
    left: 80px; top: 47px;
    font-size: 34px; line-height: 37px;
    color: var(--text-deep);
    -webkit-text-stroke: 0.6px var(--text-deep);
  }
  .handle {
    position: absolute; left: 0; right: 0;
    text-align: center;
    font-family: "Quicksand", sans-serif;
    font-size: 11px;
  }
  .post--dark .handle { top: 293px; color: var(--text-light); padding-left: 12px; }
  .post--hot .handle { top: 378px; color: var(--text-pale); padding-left: 12px; }
  .post--soft .handle { top: 391px; color: var(--text-deep); padding-left: 12px; }
</style>
</head>
<body>
<main class="series">
  <article class="post post--dark">
    <p class="quote">
      <span>Tired. Moody. Stubborn</span>
      <span>belly fat&nbsp; your hormones</span>
      <span>are screaming for help!</span>
      <span>Let’s fix that.</span>
    </p>
    <p class="handle">@TovaMarshOnline</p>
    <svg class="corner" viewBox="0 0 96 97" aria-hidden="true"><polygon points="96,0 96,97 0,97"/></svg>
  </article>

  <article class="post post--hot">
    <p class="quote">
      <span>That stubborn</span>
      <span>weight?</span>
      <span>It’s not your fault.</span>
      <span>Your hormones are</span>
      <span>to blame and</span>
      <span>you’re not alone;</span>
      <span class="indent">but there is a fix.</span>
    </p>
    <p class="handle">@TovaMarshOnline</p>
    <svg class="corner" viewBox="0 0 96 97" aria-hidden="true"><polygon points="96,0 96,97 0,97"/></svg>
  </article>

  <article class="post post--soft">
    <p class="quote">
      <span>Your belly isn’t</span>
      <span>fat . . .</span>
      <span>It’s hormonal.</span>
      <span>And here’s</span>
      <span>how to fix it.</span>
      <span>Comment</span>
      <span>hormones</span>
      <span>if nothing is</span>
      <span>working.</span>
    </p>
    <p class="handle">@TovaMarshOnline</p>
    <svg class="corner" viewBox="0 0 96 97" aria-hidden="true"><polygon points="96,0 96,97 0,97"/></svg>
  </article>
</main>
</body>
</html>
```